Kestrel Hill Historic District Banner

Our Historic district is located in Allentown Pennsylvania, USA and is in need of a new banner design. The banners measure 18" wide by 36" tall. The banners are hung upon decorative street lights approximately 7' above ground. The district is adjacent to a downtown area that is experiencing significant growth and economic revitalization. The district is in need of a banner that respects the historic nature of the neighborhood while also saying that this is a hip urban residential neighborhood. You can visit our website at www.kestrelhill.org to learn more about our district. I also will upload our current logo which we like but think it may need some freshening up. I will also upload an image of one of the light poles.

just added a sketch of one thought that came up during one of my board meetings. We like the idea of keeping it simple, bold, easy to digest. we just upgraded many of our street signs in a black and white theme. thought it could be used in a playful positive and negative fashion. we also have previously liked color combinations of gold and blue - gold and black - gold and sepia - parchment and sepia

```html
<!DOCTYPE html>
<html lang="en">
<head>
<meta charset="utf-8">
<title>Kestrel Hill Historic District Banner</title>
<link rel="stylesheet" href="https://fonts.googleapis.com/css2?family=Cinzel:wght@700&display=swap">
<style>
  :root {
    --page: #efece6;
    --parchment-light: #f3e3ad;
    --parchment: #e7cd84;
    --parchment-edge: #c9a45c;
    --sepia: #a8834a;
    --ink-blue: #3b2fa6;
    --scroll-fill: #d9c9a6;
  }
  * { box-sizing: border-box; margin: 0; padding: 0; }
  html, body {
    width: 1200px;
    height: 1000px;
    overflow: hidden;
    background: var(--page);
  }
  .canvas {
    position: relative;
    width: 1200px;
    height: 1000px;
  }
  .banner {
    position: absolute;
    left: 380px;
    top: 70px;
    width: 440px;
    height: 860px;
    background:
      radial-gradient(ellipse at 50% 45%, var(--parchment-light) 0%, var(--parchment) 62%, var(--parchment-edge) 100%);
    box-shadow: inset 0 0 40px rgba(120, 80, 30, 0.35);
  }
  .banner__hem {
    position: absolute;
    left: 0;
    width: 100%;
    height: 52px;
    background: linear-gradient(180deg, var(--parchment-edge), var(--parchment));
    opacity: 0.85;
  }
  .banner__hem--top { top: 0; }
  .banner__hem--bottom { bottom: 0; transform: scaleY(-1); }
  .emblem-area {
    position: absolute;
    left: 150px;
    top: 100px;
    width: 220px;
    height: 210px;
    background: linear-gradient(160deg, rgba(59, 47, 166, 0.28), rgba(59, 47, 166, 0.12));
  }
  .district-name {
    position: absolute;
    left: 0;
    top: 340px;
    width: 100%;
    text-align: center;
    font-family: "Cinzel", serif;
    font-weight: 700;
    color: var(--ink-blue);
    font-size: 66px;
    line-height: 1.05;
    letter-spacing: 1px;
  }
  .scroll-area {
    position: absolute;
    left: 24px;
    top: 610px;
    width: 392px;
    height: 130px;
    background: linear-gradient(180deg, var(--scroll-fill), #cdb98f);
    border-radius: 10px;
  }
  .district-label {
    position: absolute;
    left: 0;
    top: 638px;
    width: 100%;
    text-align: center;
    font-family: "Cinzel", serif;
    font-weight: 700;
    color: var(--ink-blue);
    font-size: 34px;
    line-height: 1.1;
  }
</style>
</head>
<body>
<main class="canvas">
  <section class="banner" aria-label="Kestrel Hill Historic District street banner">
    <div class="banner__hem banner__hem--top"></div>
    <div class="emblem-area" role="img" aria-label="District emblem: illustration of a historic tower with a pointed roof and arched window"></div>
    <h1 class="district-name">Kestrel<br>Hill</h1>
    <div class="scroll-area" role="img" aria-label="Ornamental unrolled parchment scroll ribbon"></div>
    <p class="district-label">Historic<br>District</p>
    <div class="banner__hem banner__hem--bottom"></div>
  </section>
</main>
</body>
</html>
```